Bramwick Client Journey To Success

I need a one-page document that graphically shows the client's journey working with Bramwick from initial assessment to completed project. I want the journey to start at the "basecamp logo" and reach 4 summits (little mountain logos...) .

I'd like the imagery to convey the client starting at basecamp, and moving to each summit. Each summit, should list the subtext under each, as listed on the pdf doc i provided.

The description for the basecamp and 4 summits is attached.

I need the brochure to look like the other brochure that you did for me (attached) .

Target Market(s)

Restaurant Owners

Industry/Entity Type

Construction Management

Font styles to use
Sans Serif

Colors
EB3D1F
EC4F4E
F09395
F8D3D4
FCEDEE

Requirements
Must have
• My logo. Title: Client Journey To Success. Subtitle: The 4 Summits

```html
<!DOCTYPE html>
<html lang="en">
<head>
<meta charset="utf-8">
<title>Bramwick Development – Client Journey to Success</title>
<link rel="stylesheet" href="https://fonts.googleapis.com/css2?family=Montserrat:ital,wght@0,500;0,600;0,700;0,800;0,900;1,500;1,800;1,900&display=swap">
<style>
  :root {
    --red: #e1252b;
    --red-deep: #b5171d;
    --ink: #111214;
    --night: #16181c;
    --grey-text: #77787b;
    --paper: #ffffff;
  }
  * { margin: 0; padding: 0; box-sizing: border-box; }
  html, body { width: 972px; height: 1200px; overflow: hidden; background: var(--paper); }
  body { font-family: "Montserrat", Arial, sans-serif; color: var(--ink); }

  .flyer { position: relative; width: 972px; height: 1200px; overflow: hidden; background: var(--paper); }
  .backdrop { position: absolute; inset: 0; }

  .brand {
    position: absolute; left: 34px; top: 0; width: 281px; height: 278px;
    display: flex; flex-direction: column; align-items: center; justify-content: flex-end;
    padding-bottom: 18px; gap: 42px;
  }
  .brand-mark { width: 92px; height: 92px; background: var(--red); }
  .brand-name { font-weight: 800; font-size: 17px; letter-spacing: 0.2px; color: var(--ink); }

  .title {
    position: absolute; right: 39px; top: 72px; text-align: right;
    color: var(--paper); font-weight: 900; font-size: 53px; line-height: 58px;
    letter-spacing: -0.5px; text-transform: uppercase;
    text-shadow: 0 3px 6px rgba(0,0,0,.45);
  }
  .subtitle-band {
    position: absolute; left: 315px; top: 200px; width: 657px; height: 63px;
    background: var(--red);
  }
  .subtitle {
    position: absolute; right: 40px; top: 4px;
    color: var(--paper); font-style: italic; font-weight: 900; font-size: 52px; line-height: 56px;
    text-transform: uppercase; letter-spacing: -0.5px;
  }

  .journey { position: absolute; left: 68px; top: 338px; width: 330px; }
  .basecamp-title { color: var(--red); font-weight: 700; font-size: 27px; line-height: 30px; letter-spacing: 0.5px; }
  .basecamp-list { list-style: none; margin-top: 4px; }
  .basecamp-list li { font-weight: 800; font-size: 18px; line-height: 26px; }

  .summit { position: absolute; left: 68px; width: 340px; }
  .summit-tag { position: relative; height: 30px; }
  .summit-tag svg { position: absolute; left: 0; top: 0; }
  .summit-tag span {
    position: absolute; left: 13px; top: 4px; color: var(--paper);
    font-weight: 700; font-size: 15px; line-height: 20px;
  }
  .summit-name { font-weight: 700; font-size: 26px; line-height: 30px; margin-top: 2px; }
  .summit-steps { list-style: none; }
  .summit-steps li { font-style: italic; font-weight: 500; font-size: 16px; line-height: 22px; color: var(--grey-text); letter-spacing: 0.3px; }

  .summit-1 { top: 477px; }
  .summit-2 { top: 690px; }
  .summit-3 { top: 833px; }
  .summit-4 { top: 1000px; }

  .footer-band {
    position: absolute; left: 0; top: 1116px; width: 575px; height: 52px;
    background: var(--ink); padding-left: 68px;
    color: var(--paper); font-weight: 700; font-size: 25px; line-height: 52px; letter-spacing: 0.3px;
  }
</style>
</head>
<body>
<main class="flyer">

  <svg class="backdrop" width="972" height="1200" viewBox="0 0 972 1200" aria-hidden="false">
    <defs>
      <linearGradient id="siteNight" x1="0" y1="0" x2="0" y2="1">
        <stop offset="0" stop-color="#2a2d31"/>
        <stop offset="1" stop-color="#0d0e10"/>
      </linearGradient>
      <linearGradient id="crewPhoto" x1="0" y1="0" x2="0" y2="1">
        <stop offset="0" stop-color="#e6e4df"/>
        <stop offset=".55" stop-color="#b9b08f"/>
        <stop offset="1" stop-color="#d8d3c8"/>
      </linearGradient>
      <linearGradient id="sparkPhoto" x1="0" y1="0" x2="1" y2="1">
        <stop offset="0" stop-color="#26282b"/>
        <stop offset=".6" stop-color="#3a3530"/>
        <stop offset="1" stop-color="#c27a3a"/>
      </linearGradient>
      <linearGradient id="interiorPhoto" x1="0" y1="0" x2="1" y2="1">
        <stop offset="0" stop-color="#f2b24a"/>
        <stop offset=".5" stop-color="#d98a2a"/>
        <stop offset="1" stop-color="#8a4a1c"/>
      </linearGradient>
      <linearGradient id="storefrontPhoto" x1="0" y1="0" x2="0" y2="1">
        <stop offset="0" stop-color="#1d3a7a"/>
        <stop offset=".45" stop-color="#d9dde3"/>
        <stop offset="1" stop-color="#8c8b86"/>
      </linearGradient>
    </defs>

    <!-- night construction backdrop -->
    <polygon points="315,0 972,0 972,560 880,520 560,410 315,330" fill="url(#siteNight)" role="img" aria-label="Night view of a timber-framed building under construction"/>
    <!-- left edge dark strip with red slant -->
    <polygon points="0,0 34,0 34,225 0,210" fill="var(--night)"/>
    <polygon points="0,210 34,218 34,243 0,226" fill="var(--red)"/>
    <!-- red diagonal ribbon under the logo panel -->
    <polygon points="315,318 420,358 560,412 527,420 315,345" fill="var(--red)"/>
    <polygon points="440,370 540,408 527,420 450,392" fill="var(--red-deep)"/>

    <!-- hexagon: crew on site -->
    <polygon points="666,286 845,341 871,506 734,612 551,559 519,392" fill="var(--red)"/>
    <polygon points="666,301 833,352 857,504 731,598 560,548 531,398" fill="url(#crewPhoto)" role="img" aria-label="Photo of three site workers in hard hats and safety vests overlooking a build"/>

    <!-- hexagon: welding sparks -->
    <polygon points="551,586 718,642 766,802 634,923 459,870 412,711" fill="var(--red)"/>
    <polygon points="553,601 707,652 751,800 630,910 470,860 427,714" fill="url(#sparkPhoto)" role="img" aria-label="Photo of a worker grinding metal with sparks flying"/>

    <!-- hexagon: restaurant interior -->
    <polygon points="766,627 881,517 972,540 972,843 869,821 777,798 740,700" fill="var(--red)"/>
    <polygon points="778,630 884,531 972,552 972,830 866,808 788,787 754,700" fill="url(#interiorPhoto)" role="img" aria-label="Photo of a warm-lit restaurant interior with patterned wall and windows"/>

    <!-- hexagon: storefront at dusk -->
    <polygon points="774,821 972,855 972,1200 575,1200 543,1037 634,931" fill="var(--red)"/>
    <polygon points="779,836 972,868 972,1200 588,1200 557,1040 643,943" fill="url(#storefrontPhoto)" role="img" aria-label="Photo of a finished restaurant storefront with red steel columns at dusk"/>
  </svg>

  <header class="brand">
    <div class="brand-mark"></div>
    <p class="brand-name">BRAMWICK DEVELOPMENT</p>
  </header>

  <h1 class="title">Client Journey<br>To Success</h1>
  <div class="subtitle-band"><h2 class="subtitle">The 4 Summits</h2></div>

  <section class="journey">
    <h3 class="basecamp-title">BASECAMP</h3>
    <ul class="basecamp-list">
      <li>a. Client Assessment</li>
      <li>b. Determine Project Goals</li>
      <li>c. Proposal &amp; Fees</li>
    </ul>
  </section>

  <section class="summit summit-1">
    <div class="summit-tag">
      <svg width="320" height="31" viewBox="0 0 320 31"><polygon points="0,0 112,0 129,29 0,29" fill="var(--red)"/><line x1="0" y1="29.5" x2="318" y2="29.5" stroke="var(--ink)" stroke-width="2"/></svg>
      <span>Summit 1</span>
    </div>
    <h4 class="summit-name">PreConstruction</h4>
    <ul class="summit-steps">
      <li>a. Develop Project Plan</li>
      <li>b. Develop Risk Assessment &amp; Plan</li>
      <li>c. Devlelop Schedule</li>
      <li>d. Develop Budget</li>
      <li>e. Develop Team</li>
      <li>f. GC, Sub, Consultants Contracts</li>
    </ul>
  </section>

  <section class="summit summit-2">
    <div class="summit-tag">
      <svg width="320" height="31" viewBox="0 0 320 31"><polygon points="0,0 112,0 129,29 0,29" fill="var(--red)"/><line x1="0" y1="29.5" x2="318" y2="29.5" stroke="var(--ink)" stroke-width="2"/></svg>
      <span>Summit 2</span>
    </div>
    <h4 class="summit-name">Execution</h4>
    <ul class="summit-steps">
      <li>a. Acquire Permits</li>
      <li>b. PreConstruction Meeting</li>
      <li>c. Project Start</li>
    </ul>
  </section>

  <section class="summit summit-3">
    <div class="summit-tag">
      <svg width="320" height="31" viewBox="0 0 320 31"><polygon points="0,0 112,0 129,29 0,29" fill="var(--red)"/><line x1="0" y1="29.5" x2="318" y2="29.5" stroke="var(--ink)" stroke-width="2"/></svg>
      <span>Summit 3</span>
    </div>
    <h4 class="summit-name">Project Management</h4>
    <ul class="summit-steps">
      <li>a. Shared Consciousness Meetings</li>
      <li>b. Pressurized Collaboration</li>
      <li>c. Schedule Management</li>
      <li>d. Run O.O.D.A. Loop</li>
    </ul>
  </section>

  <section class="summit summit-4">
    <div class="summit-tag">
      <svg width="320" height="31" viewBox="0 0 320 31"><polygon points="0,0 112,0 129,29 0,29" fill="var(--red)"/><line x1="0" y1="29.5" x2="318" y2="29.5" stroke="var(--ink)" stroke-width="2"/></svg>
      <span>Summit 4</span>
    </div>
    <h4 class="summit-name">Completion</h4>
    <ul class="summit-steps">
      <li>a. Closeout</li>
    </ul>
  </section>

  <footer class="footer-band">www.bramwickdevgroup.com</footer>
</main>
</body>
</html>
```